Ginger Beer Can Design for a none alcoholic bavarage

We need a cool, modern, fresh design for a can.

- 330ml sleek can size
- 0.0% alcohol
- BIO
- ingredience: Water, Sugar, Ginger, limejuice, Gummi Arabicum, Carbonisation
- Energy table of fats, carbs, protein, etc.
- address: Quiet Pine Fizz, Mühlengasse 18, 4062 Basel

Went on vacation/holiday

```html
<!DOCTYPE html>
<html lang="en">
<head>
<meta charset="utf-8">
<title>Ginger Beer – Can Label</title>
<link rel="stylesheet" href="https://fonts.googleapis.com/css2?family=Montserrat:wght@500;600;700;800&display=swap">
<style>
  :root {
    --stage: #1d5a80;
    --label-white: #f7f8f7;
    --gold: #b5853a;
    --gold-dark: #9a6c28;
    --ink: #1e1e1e;
    --ginger-orange: #eda565;
    --peach: #f3c99a;
    --lime: #8fc24a;
    --leaf: #4f9a2c;
    --leaf-dark: #3c7f22;
    --wave-line: #d8c27a;
    --table-line: #c99a56;
    --white: #ffffff;
  }
  * { box-sizing: border-box; margin: 0; padding: 0; }
  html, body { width: 1165px; height: 1200px; overflow: hidden; }
  body {
    background: var(--stage);
    font-family: "Montserrat", Arial, sans-serif;
    color: var(--ink);
    position: relative;
  }
  .label {
    position: absolute;
    top: 120px;
    width: 400px;
    height: 960px;
    background: var(--label-white);
    border-radius: 14px;
    overflow: hidden;
  }
  .label--front { left: 160px; }
  .label--back  { left: 605px; }

  /* Front */
  .brand {
    position: absolute; top: 48px; left: 0; right: 0;
    display: flex; flex-direction: column; align-items: center; gap: 10px;
  }
  .brand__dot {
    width: 70px; height: 70px; border-radius: 50%;
    border: 4px solid var(--leaf);
  }
  .brand__name {
    font-weight: 700; font-size: 17px; color: var(--gold-dark); letter-spacing: 0.5px;
  }
  .product-title {
    position: absolute; top: 168px; left: 0; right: 0; text-align: center;
    font-weight: 800; font-size: 70px; line-height: 0.98; color: var(--gold);
    letter-spacing: 1px;
  }
  .abv {
    position: absolute; top: 322px; left: 0; right: 0; text-align: center;
    font-weight: 700; font-size: 24px; letter-spacing: 0.5px;
  }
  .front-fade {
    position: absolute; left: 0; right: 0; top: 380px; bottom: 0;
    background: linear-gradient(180deg, rgba(247,248,247,0) 0%, var(--peach) 35%, var(--ginger-orange) 60%, var(--lime) 100%);
  }
  .illustration {
    position: absolute; top: 370px; left: 50px; width: 300px; height: 230px;
    border-radius: 40% 50% 45% 40%;
    background: radial-gradient(ellipse at 45% 45%, #d9a66a 0%, #c89257 40%, #9cc45a 75%, rgba(143,194,74,0) 100%);
  }
  .wave { position: absolute; left: 0; top: 540px; width: 400px; height: 420px; }
  .bio-badge {
    position: absolute; top: 610px; right: 44px;
    width: 78px; height: 78px; border-radius: 50%;
    border: 3px solid var(--white); background: var(--leaf);
  }
  .claim {
    position: absolute; top: 770px; left: 0; right: 0; text-align: center;
    font-weight: 700; font-size: 26px; line-height: 1.15; color: var(--white);
  }
  .volume {
    position: absolute; top: 856px; left: 0; right: 0; text-align: center;
    font-weight: 700; font-size: 32px; color: var(--white);
  }

  /* Back */
  .back-fade {
    position: absolute; left: 0; right: 0; top: 400px; bottom: 0;
    background: linear-gradient(180deg, rgba(247,248,247,0) 0%, var(--peach) 30%, #e9b26c 60%, #c9d46a 85%, var(--lime) 100%);
  }
  .ingredients {
    position: absolute; top: 60px; right: 34px; width: 340px; text-align: right;
    font-size: 19px; line-height: 1.3; font-weight: 500;
  }
  .ingredients__title { font-weight: 800; font-size: 20px; }
  .ingredients__bio { color: var(--leaf); font-weight: 800; }
  .energy-table {
    position: absolute; top: 420px; left: 40px; width: 320px;
    border: 2px solid var(--table-line); border-radius: 10px;
    background: rgba(255,255,255,0.92);
    padding: 10px 12px; font-size: 17px;
  }
  .energy-table__title { font-weight: 800; font-size: 18px; margin-bottom: 6px; }
  .energy-table table { width: 100%; border-collapse: collapse; }
  .energy-table td { border-top: 1px solid var(--table-line); padding: 3px 4px; }
  .energy-table td + td { border-left: 1px solid var(--table-line); text-align: right; width: 78px; }
  .address {
    position: absolute; bottom: 70px; right: 30px; text-align: right;
    font-size: 18px; line-height: 1.3; font-weight: 500;
  }
  .address__name { font-weight: 800; }
</style>
</head>
<body>
  <section class="label label--front">
    <div class="front-fade"></div>
    <div class="brand">
      <span class="brand__dot"></span>
      <span class="brand__name">Quiet Pine Fizz</span>
    </div>
    <h1 class="product-title">GINGER<br>BEER</h1>
    <p class="abv">0.0% ALCOHOL</p>
    <div class="illustration" role="img" aria-label="Illustration of ginger root, sliced ginger, green leaves and lime wedges"></div>
    <svg class="wave" viewBox="0 0 400 420" preserveAspectRatio="none" aria-hidden="true">
      <path d="M0 110 C 90 60, 170 150, 260 110 S 380 50, 400 75 L400 420 L0 420 Z" fill="var(--lime)"/>
      <path d="M0 145 C 100 95, 180 180, 270 145 S 380 100, 400 120 L400 420 L0 420 Z" fill="var(--leaf)"/>
      <path d="M0 180 C 110 140, 200 205, 290 172 S 380 140, 400 150" fill="none" stroke="var(--wave-line)" stroke-width="4"/>
      <path d="M0 198 C 120 160, 210 215, 400 172 L400 420 L0 420 Z" fill="var(--leaf-dark)" opacity="0.6"/>
    </svg>
    <div class="bio-badge"></div>
    <p class="claim">NON-ALCOHOLIC<br>BEVERAGE</p>
    <p class="volume">330ml</p>
  </section>

  <section class="label label--back">
    <div class="back-fade"></div>
    <div class="ingredients">
      <p class="ingredients__title">INGREDIENTS:</p>
      <p>Water, Sugar, Ginger,<br>Limejuice, Gummi Arabicum,<br>Carbonisation, <span class="ingredients__bio">BIO</span></p>
    </div>
    <div class="energy-table">
      <p class="energy-table__title">ENERGY TABLE</p>
      <table>
        <tr><td>Energy</td><td>33 kJ</td><td>13 kcal</td></tr>
        <tr><td>Fats</td><td>0 g</td><td>0 g</td></tr>
        <tr><td>Carbs</td><td>13 g</td><td>0 g</td></tr>
        <tr><td>Sugars</td><td>0 g</td><td>0 g</td></tr>
        <tr><td>Protein</td><td>12 g</td><td>0 g</td></tr>
        <tr><td>Salt</td><td>0.0 g</td><td>0 g</td></tr>
        <tr><td>Salt, etc.</td><td>0.0 g</td><td>0.008</td></tr>
      </table>
    </div>
    <div class="address">
      <p class="address__name">Quiet Pine Fizz,</p>
      <p>Mühlengasse 18, 4062 Basel</p>
    </div>
  </section>
</body>
</html>
```